Label Design for Sacha Inchi Oil in 250ml Bottle

We need unique labeling design for our product, Sacha Inchi Oil in 250ml glass bottle form. The final design should have the Company logo and the product label KAVU'S displayed. We have attached the artwork of our Company logo and the nutrients/consumption details of the product for your necessary designing. Label size for the 250ml bottle will be 122mm x 34mm.

It Company

```html
<!DOCTYPE html>
<html lang="en">
<head>
<meta charset="utf-8">
<title>KAVU'S Sacha Inchi Oil – Label Options</title>
<link href="https://fonts.googleapis.com/css2?family=Roboto+Condensed:wght@400;700&family=Source+Sans+3:wght@300;400;600;700;900&display=swap" rel="stylesheet">
<style>
:root{
  --bg:#dcdcdc;
  --green:#3db54a;
  --deep:#1f6e37;
  --band:#2f7a3f;
  --leaf:#2e7d3a;
  --brown:#3a2a1f;
  --orange:#f2a52a;
  --ink:#222;
  --table:#eef5d8;
  --white:#fff;
}
*{box-sizing:border-box;margin:0;padding:0}
html,body{width:1200px;height:1200px;overflow:hidden}
body{background:var(--bg);font-family:"Source Sans 3",Arial,sans-serif;color:var(--ink);position:relative}
.option-title{position:absolute;left:0;width:1200px;text-align:center;font-family:"Roboto Condensed",Arial,sans-serif;font-weight:400;color:var(--green);font-size:62px;line-height:1}
.option-title.d2{top:170px}
.option-title.d1{top:614px}
.label{position:absolute;left:90px;width:1020px;overflow:hidden}
.label-d2{top:281px;height:281px}
.label-d1{top:718px;height:285px;background:var(--white);border:1px solid #555}
svg.layer{position:absolute;left:0;top:0}

/* nutrition */
.nutri{position:absolute;font-size:7.6px;line-height:1.3}
.nutri h4{font-size:7.8px;font-weight:700}
.nutri table{border-collapse:collapse;width:100%;margin-top:4px}
.nutri th{font-weight:400;text-align:right;vertical-align:bottom;font-size:7.2px;line-height:1.15;padding-bottom:4px}
.nutri td{height:11.8px;white-space:nowrap}
.nutri td.num{text-align:right}
.label-d2 .nutri{left:50px;top:25px;width:380px}
.label-d2 .nutri table{background:var(--table);margin-left:-10px;width:302px}
.label-d2 .nutri td:first-child{padding-left:10px}
.label-d2 .nutri td:nth-child(2){width:80px}
.label-d2 .nutri td:nth-child(3){width:72px;padding-right:8px}
.label-d1 .nutri{left:18px;top:12px;width:300px}
.label-d1 .nutri td{height:10px;line-height:10px}
.label-d1 .nutri td:nth-child(2){width:80px}
.label-d1 .nutri td:nth-child(3){width:72px}

/* info column */
.info{position:absolute;font-size:7.4px;line-height:8.8px}
.info h4{font-size:9px;font-weight:700;line-height:10px}
.info p{margin-bottom:6px}
.label-d2 .info{left:688px;top:33px;width:305px}
.label-d1 .info{left:667px;top:17px;width:350px}
.info-cols{display:flex;gap:7px}
.info-cols .packed{width:148px}
.info-cols .owner{width:192px}
.info-cols h4{font-size:8.8px;white-space:nowrap}

/* decoration placeholders */
.leaf-pattern{position:absolute;background:linear-gradient(180deg,#e4e4e4,#d2d2d2);border-radius:4px}
.mark{position:absolute;border-radius:50%;border:3px solid var(--brown)}
.capsules{position:absolute;border-radius:50%;background:radial-gradient(ellipse at 45% 45%,#f7c95a,#d98a14 60%,rgba(217,138,20,0) 72%)}
.brand{position:absolute;font-weight:900;text-align:center;line-height:1}
.badge-ring{position:absolute;border:1.5px solid #333;border-radius:50%;font-family:"Roboto Condensed",sans-serif;font-weight:700;text-align:center;transform:rotate(14deg)}
.center-d2{position:absolute;left:395px;width:230px;text-align:center}
.cold{font-family:"Roboto Condensed",Arial,sans-serif;font-weight:700;font-size:17px;line-height:18px;color:var(--brown)}
.malay{font-weight:300;font-size:13.4px;line-height:16px}
.omega{font-size:14.5px;font-weight:400;line-height:18px}
.vol-line{line-height:16px;height:16px}
.vol{font-size:7px;color:#555;line-height:7.4px;text-align:left;display:inline-block;vertical-align:bottom}
.vol-big{font-size:17px;font-weight:300;line-height:16px;vertical-align:bottom;margin-left:4px}
.mrp{position:absolute;font-size:7.6px;line-height:1.1}
.mrp b{font-size:9px}
.batch{position:absolute;font-size:7.4px;line-height:1.4;white-space:nowrap}

/* D1 specifics */
.glow{position:absolute;left:360px;top:-40px;width:300px;height:360px;border-radius:50%;background:radial-gradient(ellipse at 50% 45%,#ffffff 35%,#e6f2dc 60%,#b9d9a6 80%,rgba(185,217,166,0) 100%)}
.badge-d1{position:absolute;left:368px;top:106px;width:50px;height:50px;border-radius:12px;background:var(--leaf);transform:rotate(-20deg);color:var(--white);font-family:"Roboto Condensed",sans-serif;font-weight:700;text-align:center;font-size:15px;line-height:1;padding-top:10px;border:2px solid #fff;box-shadow:0 0 0 1px #ccc}
.badge-d1 span{display:block;font-size:7px;font-weight:400}
.omega-d1{position:absolute;left:400px;width:220px;top:158px;text-align:center;font-weight:900;font-size:21px;color:#d4870d}
.sub-d1{position:absolute;left:400px;width:220px;top:192px;text-align:center;font-family:"Roboto Condensed",sans-serif;font-size:8.6px;line-height:1.25;color:var(--ink)}
.pill{position:absolute;left:406px;top:222px;width:142px;height:36px;background:var(--white);border-radius:18px;text-align:center;color:var(--leaf);box-shadow:0 1px 3px rgba(0,0,0,.2)}
.pill b{display:block;font-family:"Roboto Condensed",sans-serif;font-size:13px;padding-top:4px}
.pill small{display:block;font-size:8.6px;font-weight:700}
.white{color:var(--white)}
</style>
</head>
<body>

<div class="option-title d2">D2</div>

<section class="label label-d2">
  <svg class="layer" width="1020" height="281" viewBox="0 0 1020 281">
    <rect width="1020" height="281" fill="var(--green)"/>
    <rect x="10" y="10" width="1000" height="261" fill="var(--white)"/>
    <rect x="20" y="24" width="980" height="240" fill="none" stroke="var(--deep)" stroke-width="2.5"/>
    <path d="M393,24 C410,24 412,8 432,8 L588,8 C608,8 610,24 627,24 L627,264 C610,264 608,274 588,274 L432,274 C412,274 410,264 393,264 Z" fill="var(--white)"/>
    <path d="M393,24 C410,24 412,8 432,8 L588,8 C608,8 610,24 627,24" fill="none" stroke="var(--deep)" stroke-width="2.5"/>
    <path d="M393,264 C410,264 412,274 432,274 L588,274 C608,274 610,264 627,264" fill="none" stroke="var(--deep)" stroke-width="2.5"/>
  </svg>

  <div class="nutri">
    <h4>Maklumat Pemakanan / Nutrition Information</h4>
    <div>Saiz Hidangan / Serving Size: 1 sudu camca / 1 tablespoon (15ml)</div>
    <div>Hidangan Setiap Botol / Serving Per Bottle: 16</div>
    <table>
      <tr><th></th><th>Setiap / Per 100ml</th><th>Setiap Hidangan /<br>Per Serving 15ml</th></tr>
      <tr><td>Tenaga / Energy</td><td class="num">806 kcal (3385 kJ)</td><td class="num">121 kCal (508 kJ)</td></tr>
      <tr><td>Protein / Protein</td><td class="num">0 g</td><td class="num">0 g</td></tr>
      <tr><td>Karbohidrat / Carbohydrate</td><td class="num">18.3 g</td><td class="num">2.7 g</td></tr>
      <tr><td>Lemak / Fat yang terdiri daripada /</td><td></td><td></td></tr>
      <tr><td>comprising of</td><td class="num">81.4 g</td><td class="num">12.2 g</td></tr>
      <tr><td>Asid Lemak Monotidaktepu /</td><td></td><td></td></tr>
      <tr><td>Monounsaturated Fatty Acid</td><td class="num">4.6 g</td><td class="num">0.7 g</td></tr>
      <tr><td>Omega-9</td><td class="num">4.4 g</td><td class="num">0.7 g</td></tr>
      <tr><td>Asid Lemak Politidaktepu /</td><td></td><td></td></tr>
      <tr><td>Polyunsaturated Fatty Acid</td><td class="num">71.7 g</td><td class="num">10.8 g</td></tr>
      <tr><td>Omega-3</td><td class="num">44.1 g</td><td class="num">6.6 g</td></tr>
      <tr><td>Omega-6</td><td class="num">27.5 g</td><td class="num">4.1 g</td></tr>
      <tr><td>Asid LemakTepu / Saturated Fatty Acid</td><td class="num">5.1 g</td><td class="num">0.8 g</td></tr>
      <tr><td>Asid Trans Lemak / Trans Fatty Acid</td><td class="num">0.1 g</td><td class="num">0 g</td></tr>
      <tr><td>Kolesterol / Cholesterol</td><td class="num">0 g</td><td class="num">0 g</td></tr>
    </table>
  </div>

  <div class="leaf-pattern" style="left:348px;top:28px;width:54px;height:232px" role="img" aria-label="Column of outlined leaf pattern"></div>
  <div class="leaf-pattern" style="left:622px;top:28px;width:54px;height:232px" role="img" aria-label="Column of outlined leaf pattern"></div>

  <div class="mark" style="left:486px;top:33px;width:48px;height:48px"></div>
  <div class="brand" style="left:430px;width:160px;top:104px;font-size:31px;color:var(--brown)">KAVU'S</div>
  <div class="capsules" style="left:453px;top:136px;width:108px;height:48px" role="img" aria-label="Golden oil softgel capsules"></div>
  <div class="badge-ring" style="left:561px;top:130px;width:50px;height:36px;font-size:11px;line-height:1;padding-top:6px">100%<br><span style="font-size:6.5px;font-weight:400">PUREASLI</span></div>

  <div class="center-d2" style="top:176px">
    <div class="cold">Cold Pressed<br>Sacha Inchi Oil</div>
    <div class="malay">Minyak Sacha Inchi Perahan Sejuk</div>
    <div class="omega">Omega 3, 6, 9</div>
    <div class="vol-line"><span class="vol">Isipadu Minima<br>Minimum Volume</span><span class="vol-big">250 ml</span></div>
  </div>

  <div class="info">
    <h4>Arahan Penggunaan / Directions For Use</h4>
    <p>Campurkan 1 sudu camca minyak ke dalam salad dan gaul bersama. /<br>Mix 1 tablespoon of oil into salad and mix well together.</p>
    <h4>Penyimpanan / Storage</h4>
    <p>Simpan di tempat yang dingin, kering dan jauhi daripada haba dan<br>sinaran cahaya matahari./ Store in a cold and<br>dry place away from heat and direct sunlight.</p>
    <h4>Empunya Hak Untuk Mengilang / Owner of the Rights of Manufacture</h4>
    <p>Kavu Harvest Marketing Sdn. Bhd. (1000001) 12, Jalan Cempaka 3, Taman Sri Hijau,<br>81200 Johor Bahru,<br>Malaysia Tel 07 000 1234 &nbsp;Fax 07 000 5678<br>Email hello@kavuharvest.example Website kavuharvest.example<br>Hotline 010 000 2468 Wechat kavuharvest</p>
    <h4>Dibungkus Oleh / Packed by</h4>
    <p>Green Ridge Contract Packing (GMP) Sdn. Bhd. 5, Jalan Perindustrian 7,<br>Taman Perindustrian Seri, 47100 Puchong, Selangor, Malaysia</p>
    <h4>Under Owner of the Rights of Manufacture</h4>
    <p>Kavu Trading Pte. Ltd.<br>Company Registration No. 200000001K<br>9 Orchid Lane<br># 01-01 Orchid Lane Singapore 100001</p>
  </div>
  <div class="mrp" style="left:910px;top:211px">MRP:<br><b>20 $</b></div>
  <div class="batch" style="left:857px;top:238px;line-height:1.3">NO. KELOMPOK / BATCH NO.: 1234<br>TH AKHIR / EXP. DATE: 01/01/2020</div>
</section>

<div class="option-title d1">D1</div>

<section class="label label-d1">
  <div class="glow" role="img" aria-label="Soft green leaf swooshes behind the centre panel"></div>
  <svg class="layer" width="1020" height="285" viewBox="0 0 1020 285">
    <path d="M0,234 C120,222 300,210 376,285" fill="none" stroke="var(--orange)" stroke-width="4"/>
    <path d="M0,240 C120,228 290,218 366,285 L0,285 Z" fill="var(--band)"/>
    <path d="M586,285 C650,240 820,228 1020,216" fill="none" stroke="var(--orange)" stroke-width="4"/>
    <path d="M596,285 C660,246 820,234 1020,222 L1020,285 Z" fill="var(--band)"/>
  </svg>

  <div class="nutri">
    <h4>Maklumat Pemakanan / Nutrition Information</h4>
    <div>Saiz Hidangan / Serving Size: 1 sudu camca / 1 tablespoon (15ml)</div>
    <div>Hidangan Setiap Botol / Serving Per Bottle: 16</div>
    <table>
      <tr><th></th><th>Setiap / Per 100ml</th><th>Setiap Hidangan /<br>Per Serving 15ml</th></tr>
      <tr><td>Tenaga / Energy</td><td class="num">806 kcal (3385 kJ)</td><td class="num">121 kCal (508 kJ)</td></tr>
      <tr><td>Protein / Protein</td><td class="num">0 g</td><td class="num">0 g</td></tr>
      <tr><td>Karbohidrat / Carbohydrate</td><td class="num">18.3 g</td><td class="num">2.7 g</td></tr>
      <tr><td>Lemak / Fat yang terdiri daripada /</td><td></td><td></td></tr>
      <tr><td>comprising of</td><td class="num">81.4 g</td><td class="num">12.2 g</td></tr>
      <tr><td>Asid Lemak Monotidaktepu /</td><td></td><td></td></tr>
      <tr><td>Monounsaturated Fatty Acid</td><td class="num">4.6 g</td><td class="num">0.7 g</td></tr>
      <tr><td>Omega-9</td><td class="num">4.4 g</td><td class="num">0.7 g</td></tr>
      <tr><td>Asid Lemak Politidaktepu /</td><td></td><td></td></tr>
      <tr><td>Polyunsaturated Fatty Acid</td><td class="num">71.7 g</td><td class="num">10.8 g</td></tr>
      <tr><td>Omega-3</td><td class="num">44.1 g</td><td class="num">6.6 g</td></tr>
      <tr><td>Omega-6</td><td class="num">27.5 g</td><td class="num">4.1 g</td></tr>
      <tr><td>Asid LemakTepu / Saturated Fatty Acid</td><td class="num">5.1 g</td><td class="num">0.8 g</td></tr>
      <tr><td>Asid Trans Lemak / Trans Fatty Acid</td><td class="num">0.1 g</td><td class="num">0 g</td></tr>
      <tr><td>Kolesterol / Cholesterol</td><td class="num">0 g</td><td class="num">0 g</td></tr>
    </table>
  </div>

  <div class="mark" style="left:455px;top:24px;width:56px;height:56px"></div>
  <div class="badge-d1">100%<span>PUREASLI</span></div>
  <div class="brand" style="left:425px;width:130px;top:111px;font-size:34px;color:var(--leaf)">KAVU'S</div>
  <div class="omega-d1">Omega 3, 6, 9</div>
  <div class="sub-d1">Cold Pressed Sacha Inchi Oil<br>Minyak Sacha Inchi Perahan Sejuk</div>
  <div class="pill"><b>Sacha Inchi Oil</b><small>Minimum Volum 250ml</small></div>

  <div class="mrp white" style="left:84px;top:248px">MRP:<br><b>20 $</b></div>

  <div class="info">
    <h4>Arahan Penggunaan / Directions For Use</h4>
    <p>Campurkan 1 sudu camca minyak ke dalam salad dan gaul bersama. /<br>Mix 1 tablespoon of oil into salad and mix well together.</p>
    <h4>Penyimpanan / Storage</h4>
    <p>Simpan di tempat yang dingin, kering dan jauhi daripada haba dan<br>sinaran cahaya matahari./ Store in a cold and<br>dry place away from heat and direct sunlight.</p>
    <h4>Empunya Hak Untuk Mengilang / Owner of the Rights of Manufacture</h4>
    <p>Kavu Harvest Marketing Sdn. Bhd. (1000001) 12, Jalan Cempaka 3, Taman Sri Hijau,<br>81200 Johor Bahru,<br>Malaysia Tel 07 000 1234 &nbsp;Fax 07 000 5678<br>Email hello@kavuharvest.example Website kavuharvest.example<br>Hotline 010 000 2468 Wechat kavuharvest</p>
    <div class="info-cols">
      <div class="packed">
        <h4>Dibungkus Oleh / Packed by</h4>
        <p>Green Ridge Contract Packing<br>(GMP) Sdn. Bhd. 5, Jalan Perindustrian 7,<br>Taman Perindustrian Seri,<br>47100 Puchong, Selangor, Malaysia</p>
      </div>
      <div class="owner">
        <h4>Under Owner of the Rights of Manufacture</h4>
        <p>Kavu Trading Pte. Ltd.<br>Company Registration No. 200000001K<br>9 Orchid Lane<br># 01-01 Orchid Lane Singapore 100001</p>
      </div>
    </div>
  </div>
  <div class="batch white" style="left:822px;top:242px">NO. KELOMPOK / BATCH NO.: 1234<br>TH AKHIR / EXP. DATE: 01/01/2020</div>
</section>

</body>
</html>
```